Poster Design Project

I want word type poster for one place in london that will describe with words.I have attach one mine photo and two relevant text that will describe my city tybe project for the city of london at Fenwold Park.I want something like the eco-typography that I have attach.

Target Market(s)

my audience are adults 20-60

```html
<!DOCTYPE html>
<html lang="en">
<head>
<meta charset="utf-8">
<title>Fenwold Park — London</title>
<link rel="stylesheet" href="https://fonts.googleapis.com/css2?family=Bebas+Neue&family=Oswald:wght@400;500&display=swap">
<style>
  :root {
    --sky-top: #3f6fae;
    --sky-mid: #9fb3c9;
    --branches: #7a5a44;
    --trunks: #4a3429;
    --grass: #7f8a3c;
    --path: #a8896b;
    --path-dark: #6e5645;
    --ink: #ffffff;
    --badge-ink: #2a2420;
  }
  html, body {
    margin: 0;
    padding: 0;
    overflow: hidden;
    background: #1c1714;
  }
  .poster {
    position: relative;
    width: 849px;
    height: 1200px;
    overflow: hidden;
  }
  .poster__photo {
    position: absolute;
    inset: 0;
    background:
      linear-gradient(180deg,
        var(--sky-top) 0%,
        var(--sky-mid) 22%,
        var(--branches) 45%,
        var(--trunks) 60%,
        var(--grass) 66%,
        var(--grass) 71%,
        var(--path) 78%,
        var(--path-dark) 100%);
  }
  .poster__type {
    position: absolute;
    inset: 0;
  }
  .word { fill: var(--ink); }
  .display { font-family: "Bebas Neue", "Oswald", sans-serif; }
  .label { font-family: "Oswald", sans-serif; font-weight: 500; }
  .badge-circle { fill: var(--ink); }
  .badge-text { fill: var(--badge-ink); font-family: "Bebas Neue", sans-serif; }
  .bracket { stroke: var(--ink); stroke-width: 1.5; fill: none; }
</style>
</head>
<body>
<main class="poster">
  <div class="poster__photo" role="img" aria-label="Photograph of a park in winter: gulls flying over bare trees against a blue sky, a green lawn, and people resting on a bench by the path with swans and pigeons"></div>

  <svg class="poster__type" width="849" height="1200" viewBox="0 0 849 1200" aria-label="Fenwold Park was created to satisfy a royal passion for hunting. But over the years it became a place where people have pursued many other pleasures. Fenwold Park provides a unique habitat in the heart of London for a diverse variety of flora and fauna. The trees, shrub beds and herbaceous plantings provide rich habitats for song birds. London.">
    <!-- headline block -->
    <text class="word label" x="82" y="104" font-size="44" textLength="258" lengthAdjust="spacingAndGlyphs">FENWOLD PARK</text>
    <text class="word label" font-size="30" textLength="45" lengthAdjust="spacingAndGlyphs" transform="translate(347 68) rotate(90)">WAS</text>
    <circle class="badge-circle" cx="478" cy="117" r="25"/>
    <text class="badge-text" x="478" y="131" font-size="38" text-anchor="middle">TO</text>
    <text class="word display" x="269" y="165" font-size="58" textLength="148" lengthAdjust="spacingAndGlyphs">CREATED</text>
    <text class="word label" x="82" y="217" font-size="46" textLength="340" lengthAdjust="spacingAndGlyphs">SATISFY A</text>
    <text class="word display" x="212" y="342" font-size="166" textLength="295" lengthAdjust="spacingAndGlyphs">ROYAL</text>
    <text class="word label" font-size="30" textLength="99" lengthAdjust="spacingAndGlyphs" transform="translate(542 347) rotate(-90)">PASSION</text>
    <text class="word display" x="569" y="276" font-size="70" textLength="82" lengthAdjust="spacingAndGlyphs">FOR</text>
    <text class="word display" x="569" y="342" font-size="84" textLength="195" lengthAdjust="spacingAndGlyphs">HUNTING.</text>

    <!-- second sentence -->
    <text class="word display" x="31" y="443" font-size="112" textLength="340" lengthAdjust="spacingAndGlyphs">BUT OVER</text>
    <text class="word display" x="389" y="396" font-size="48" textLength="174" lengthAdjust="spacingAndGlyphs">THE YEARS</text>
    <text class="word display" x="389" y="439" font-size="48" textLength="135" lengthAdjust="spacingAndGlyphs">IT BECAME</text>
    <circle class="badge-circle" cx="576" cy="400" r="5"/>
    <text class="word display" x="591" y="396" font-size="48" textLength="131" lengthAdjust="spacingAndGlyphs">A PLACE</text>
    <text class="word display" x="591" y="439" font-size="48" textLength="131" lengthAdjust="spacingAndGlyphs">WHERE</text>
    <text class="word label" font-size="22" textLength="74" lengthAdjust="spacingAndGlyphs" transform="translate(746 439) rotate(-90)">PEOPLE</text>
    <text class="word label" font-size="22" textLength="50" lengthAdjust="spacingAndGlyphs" transform="translate(767 439) rotate(-90)">HAVE</text>
    <text class="word label" font-size="24" textLength="99" lengthAdjust="spacingAndGlyphs" transform="translate(792 439) rotate(-90)">PURSUED</text>
    <text class="word display" x="641" y="535" font-size="112" textLength="187" lengthAdjust="spacingAndGlyphs">MANY</text>
    <text class="word display" x="618" y="623" font-size="112" textLength="210" lengthAdjust="spacingAndGlyphs">OTHER</text>
    <text class="word display" x="457" y="703" font-size="104" textLength="371" lengthAdjust="spacingAndGlyphs">PLEASURES</text>

    <!-- habitat paragraph -->
    <text class="word label" x="31" y="505" font-size="30" textLength="323" lengthAdjust="spacingAndGlyphs">FENWOLD PARK PROVIDES</text>
    <text class="word label" x="31" y="544" font-size="30" textLength="323" lengthAdjust="spacingAndGlyphs">A UNIQUE HABITAT IN</text>
    <text class="word label" x="31" y="583" font-size="30" textLength="323" lengthAdjust="spacingAndGlyphs">THE HEART OF LONDON</text>
    <text class="word display" font-size="52" textLength="102" lengthAdjust="spacingAndGlyphs" transform="translate(375 453) rotate(90)">FOR</text>
    <path class="bracket" d="M416 450 H424 V623 H416"/>
    <text class="word label" font-size="56" textLength="280" lengthAdjust="spacingAndGlyphs" transform="translate(311 648) scale(-1 1)">DIVERSE</text>
    <text class="word display" x="357" y="665" font-size="100" textLength="32" lengthAdjust="spacingAndGlyphs">A</text>
    <text class="word label" x="31" y="736" font-size="46" textLength="360" lengthAdjust="spacingAndGlyphs">VARIETY OF FLORA</text>
    <text class="word label" x="328" y="764" font-size="30" textLength="63" lengthAdjust="spacingAndGlyphs">AND</text>
    <text class="word label" x="304" y="809" font-size="40" textLength="99" lengthAdjust="spacingAndGlyphs">FAUNA.</text>

    <!-- songbird paragraph -->
    <text class="word label" x="31" y="880" font-size="36" textLength="323" lengthAdjust="spacingAndGlyphs">THE TREES SHRUB BEDS</text>
    <text class="word label" x="31" y="923" font-size="36" textLength="430" lengthAdjust="spacingAndGlyphs">AND HERBAEOUS PLANTINGS</text>
    <text class="word label" x="31" y="965" font-size="36" textLength="440" lengthAdjust="spacingAndGlyphs">PROVIDE RICH HABITATS FOR</text>
    <text class="word label" font-size="32" textLength="106" lengthAdjust="spacingAndGlyphs" transform="translate(477 856) rotate(90)">SONG</text>
    <text class="word label" font-size="32" textLength="112" lengthAdjust="spacingAndGlyphs" transform="translate(531 850) rotate(90)">BIRDS</text>

    <!-- city mark -->
    <text class="word label" x="424" y="1146" font-size="32" font-weight="400" text-anchor="middle" letter-spacing="8">LONDON</text>
  </svg>
</main>
</body>
</html>
```